Business card - mobile service

O KiraTel is a mobile family safety service based on tablets and smartphones.
The business card must have:
BASIC INFO
Company Logo
Name
Position / Job Title: Co-founder
Mobile Phone Number: +55 (11) 5080 6172
Land Line: +55 (11) 9087 614352
Email Address: name@kiratel-example.com
Web Site URL: www.kiratel-example.com
PROMOTIONAL INFO
Try KiraTel free Today!
Your personal promo code: xxxx-2222-uuuu-7777-1234
Promo code text explanation with the instructions about the trial offer
Updates
Dears,
One more must have: the KiraTel slogan:
Industry/Entity Type
Safety
Look and feel
Each slider illustrates characteristics of the customer's brand and the style your logo design should communicate.

```html
<!DOCTYPE html>
<html lang="en">
<head>
<meta charset="utf-8">
<title>KiraTel Business Card</title>
<link href="https://fonts.googleapis.com/css2?family=Arimo:wght@400;700&display=swap" rel="stylesheet">
<style>
  :root {
    --backdrop: #3b3b3d;
    --card: #ffffff;
    --brand-cyan: #1ba9e1;
    --brand-blue: #1a8fd0;
    --bar-blue: #2b9ee0;
    --bar-pale: #d9eefa;
    --ink: #333333;
    --muted: #8a8a8a;
  }
  * { box-sizing: border-box; margin: 0; padding: 0; }
  html, body {
    width: 1200px; height: 900px; overflow: hidden;
    background: var(--backdrop);
    font-family: "Arimo", Arial, sans-serif;
  }
  .stage { position: relative; width: 1200px; height: 900px; }
  .card {
    position: absolute; left: 270px;
    width: 660px; height: 360px;
    background: var(--card);
    border-radius: 22px;
    overflow: hidden;
  }
  .card--front { top: 50px; }
  .card--back { top: 485px; }

  /* front */
  .brand-name {
    position: absolute; font-weight: 700; color: var(--brand-cyan);
    letter-spacing: -1px; line-height: 1;
  }
  .card--front .brand-name { left: 24px; top: 24px; font-size: 46px; }
  .slogan { position: absolute; font-weight: 700; color: var(--brand-blue); }
  .card--front .slogan { left: 24px; top: 76px; font-size: 17px; }
  .holder { position: absolute; right: 36px; top: 28px; text-align: center; }
  .holder__name { font-size: 22px; color: var(--brand-blue); }
  .holder__role { font-size: 15px; color: var(--muted); margin-top: 4px; }

  .soft-bars {
    position: absolute; left: 18px; right: 18px;
    background: linear-gradient(180deg, rgba(217,238,250,0) 0%, var(--bar-pale) 45%, rgba(217,238,250,0) 100%);
  }
  .card--front .soft-bars { top: 95px; height: 220px; opacity: 0.8; }

  .promo-band {
    position: absolute; left: 0; right: 0; top: 146px; height: 82px;
    background: var(--brand-cyan); color: #fff; text-align: center;
  }
  .promo-band__headline { font-size: 27px; font-weight: 700; margin-top: 6px; }
  .promo-band__code { font-size: 19px; margin-top: 4px; letter-spacing: 0.5px; }
  .promo-band__note { font-size: 11.5px; margin-top: 4px; }

  .contacts {
    position: absolute; left: 14px; right: 18px; top: 313px;
    display: flex; justify-content: space-between; font-size: 15px; color: var(--ink);
  }
  .contact { display: flex; align-items: center; gap: 5px; }
  .contact svg { flex: none; }
  .web {
    position: absolute; left: 0; right: 0; top: 337px;
    display: flex; justify-content: center; align-items: center; gap: 6px;
    font-size: 15px; color: var(--ink);
  }

  /* back */
  .bars-band {
    position: absolute; left: 22px; right: 22px; height: 96px;
  }
  .bars-band--top {
    top: 0;
    background: linear-gradient(180deg, var(--bar-blue) 0%, #7cc4ee 55%, rgba(217,238,250,0.2) 100%);
  }
  .bars-band--bottom {
    bottom: 0;
    background: linear-gradient(0deg, var(--bar-blue) 0%, #7cc4ee 55%, rgba(217,238,250,0.2) 100%);
  }
  .back-lockup { position: absolute; left: 0; right: 0; top: 118px; text-align: center; }
  .card--back .brand-name { position: static; font-size: 66px; }
  .card--back .slogan { position: static; font-size: 22px; margin-top: 10px; }
</style>
</head>
<body>
<main class="stage">

  <section class="card card--front">
    <div class="soft-bars" role="img" aria-label="Faint pale blue equalizer bar pattern"></div>
    <div class="brand-name">KiraTel</div>
    <div class="slogan">Your Family Safety Service</div>
    <div class="holder">
      <div class="holder__name">Your Name Here</div>
      <div class="holder__role">Principal</div>
    </div>

    <div class="promo-band">
      <div class="promo-band__headline">Try KiraTel free Today!</div>
      <div class="promo-band__code">Your personal promo code: xxxx-2222-uuuu-7777-1234</div>
      <div class="promo-band__note">Promo code text explanation with the instructions about the trial offer</div>
    </div>

    <div class="contacts">
      <span class="contact">
        <svg width="22" height="16" viewBox="0 0 22 16"><path d="M2 6c0-3 4-4 9-4s9 1 9 4v1h-5V5H7v2H2z" fill="var(--brand-blue)"/><rect x="4" y="8" width="14" height="7" rx="2" fill="var(--brand-blue)"/></svg>
        +55 (11) 9087 614352
      </span>
      <span class="contact">
        <svg width="11" height="18" viewBox="0 0 11 18"><rect x="1" y="1" width="9" height="16" rx="2" fill="none" stroke="var(--brand-blue)" stroke-width="1.6"/><rect x="3" y="4" width="5" height="7" fill="var(--brand-blue)"/></svg>
        +55 (11) 5080 6172
      </span>
      <span class="contact">
        <svg width="20" height="14" viewBox="0 0 20 14"><rect width="20" height="14" rx="2" fill="var(--brand-cyan)"/><path d="M1 1l9 7 9-7" fill="none" stroke="#fff" stroke-width="1.4"/></svg>
        name@kiratel-example.com
      </span>
    </div>
    <div class="web">
      <svg width="18" height="18" viewBox="0 0 18 18"><circle cx="9" cy="9" r="8" fill="none" stroke="var(--brand-blue)" stroke-width="1.6"/><text x="9" y="13" text-anchor="middle" font-size="10" font-weight="700" fill="var(--brand-blue)" font-family="Arimo, sans-serif">w</text></svg>
      www.kiratel-example.com
    </div>
  </section>

  <section class="card card--back">
    <div class="bars-band bars-band--top" role="img" aria-label="Blue equalizer bars hanging from the top edge"></div>
    <div class="back-lockup">
      <div class="brand-name">KiraTel</div>
      <div class="slogan">Your Family Safety Service</div>
    </div>
    <div class="bars-band bars-band--bottom" role="img" aria-label="Blue equalizer bars rising from the bottom edge"></div>
  </section>

</main>
</body>
</html>
```